Create banners that convert viewers into buyers!

We provide Online Marketing Solutions for small to medium size businesses from web design, Local SEO, Pay-Per-Click, Social Media and Content Marketing. We've been helping local businesses since 2009 and offer a very high level of service that is rarely matched.

Really like to stay colors of logo like banner ad ideas 2 sample.

Would also like to use a photo of a responsive web design as attached image. (you may use a different layout as image provided may be to big for some dimensions)

Sizes needed:
728x90
300x250
480x60

Add Slogan: We Drive Traffic & Phone Calls!

Slogan: We Drive Phone Calls & Conversions

Small to Medium Size businesses: Main businesses we work with are Home Improvement, Lawyers & Physicians

Marketing

```html
<!DOCTYPE html>
<html lang="en">
<head>
<meta charset="utf-8">
<title>Banner Set – We Drive Phone Calls &amp; Conversions</title>
<link href="https://fonts.googleapis.com/css2?family=PT+Sans:wght@400;700&display=swap" rel="stylesheet">
<style>
  :root{
    --page:#ffffff;
    --navy-deep:#020a1c;
    --navy:#0a2350;
    --band-light:#cfe3f6;
    --band-mid:#7fb2e4;
    --band-edge:#3d86cf;
    --logo-ink:#143a7a;
    --bullet:#3a9bf0;
    --text-light:#ffffff;
    --text-dark:#0d1f3c;
    --btn-top:#ffd84a;
    --btn-bot:#f5a300;
    --btn-edge:#b86f00;
    --frame:#1a1a1a;
  }
  html,body{margin:0;padding:0;width:1200px;height:755px;overflow:hidden;background:var(--page);}
  .stage{position:relative;width:750px;height:472px;transform:scale(1.6);transform-origin:0 0;font-family:"PT Sans",Arial,sans-serif;}
  .banner{position:absolute;overflow:hidden;border:1px solid var(--frame);box-sizing:border-box;
    background:
      radial-gradient(ellipse 40% 90% at 30% 40%, rgba(40,110,200,.55), transparent 70%),
      radial-gradient(ellipse 30% 80% at 75% 30%, rgba(30,90,180,.45), transparent 70%),
      linear-gradient(180deg,var(--navy) 0%,var(--navy-deep) 100%);}
  .device-art{position:absolute;border-radius:3px;
    background:linear-gradient(135deg,#2b3440 0%,#b9c2cc 45%,#d64a2a 60%,#1c2230 100%);}
  .headline{position:absolute;margin:0;color:var(--text-light);font-weight:700;line-height:1.08;white-space:nowrap;text-shadow:0 1px 2px rgba(0,0,0,.6);}
  .services{position:absolute;margin:0;padding:0;list-style:none;color:var(--text-light);}
  .services li{display:flex;align-items:center;white-space:nowrap;}
  .services li::before{content:"";display:inline-block;width:0;height:0;border-style:solid;border-color:transparent transparent transparent var(--bullet);margin-right:5px;}
  .brand-panel{position:absolute;background:linear-gradient(180deg,var(--band-light) 0%,var(--band-mid) 70%,var(--band-edge) 100%);}
  .brand-name{position:absolute;margin:0;color:var(--logo-ink);font-weight:700;white-space:nowrap;line-height:1;text-align:center;}
  .brand-name span{display:block;}
  .site-url{position:absolute;margin:0;color:var(--text-dark);white-space:nowrap;}
  .cta{position:absolute;display:flex;align-items:center;justify-content:center;gap:4px;box-sizing:border-box;
    background:linear-gradient(180deg,var(--btn-top),var(--btn-bot));border:1px solid var(--btn-edge);border-radius:4px;
    color:#111;white-space:nowrap;}
  .cta svg{flex:none;}

  /* 300 x 250 */
  .banner--rect{left:222px;top:15px;width:302px;height:252px;}
  .banner--rect .headline{left:0;right:0;top:8px;text-align:center;font-size:25px;}
  .banner--rect .device-art{left:5px;top:84px;width:166px;height:116px;}
  .banner--rect .services{left:179px;top:94px;font-size:13.5px;line-height:17px;}
  .banner--rect .services li::before{border-width:4px 0 4px 6px;}
  .banner--rect .brand-panel{left:0;right:0;top:200px;bottom:0;}
  .banner--rect .brand-name{left:8px;top:6px;font-size:17px;}
  .banner--rect .brand-name span + span{font-size:7px;letter-spacing:3.6px;margin-top:2px;}
  .banner--rect .site-url{left:24px;top:35px;font-size:12px;}
  .banner--rect .cta{left:168px;top:10px;width:114px;height:31px;font-size:16px;}

  /* 728 x 90 */
  .banner--leader{left:8px;top:281px;width:730px;height:91px;}
  .banner--leader .device-art{left:4px;top:6px;width:133px;height:80px;}
  .banner--leader .headline{left:154px;top:16px;font-size:27px;}
  .banner--leader .services{left:446px;top:9px;font-size:12.5px;line-height:15px;}
  .banner--leader .services li::before{border-width:3px 0 3px 5px;}
  .banner--leader .brand-panel{left:575px;top:0;right:0;bottom:0;}
  .banner--leader .brand-name{left:14px;top:8px;font-size:17px;}
  .banner--leader .brand-name span + span{font-size:7px;letter-spacing:3.6px;margin-top:1px;}
  .banner--leader .site-url{left:24px;top:37px;font-size:12px;}
  .banner--leader .cta{left:23px;top:54px;width:114px;height:30px;font-size:16px;}

  /* 480 x 60 (shown at 470 x 59) */
  .banner--strip{left:8px;top:383px;width:470px;height:59px;}
  .banner--strip .device-art{left:3px;top:5px;width:98px;height:50px;}
  .banner--strip .headline{left:110px;top:6px;font-size:15.5px;}
  .banner--strip .services{left:148px;top:30px;width:215px;font-size:10px;line-height:12px;display:flex;flex-wrap:wrap;column-gap:6px;}
  .banner--strip .services li::before{border-width:3px 0 3px 4px;margin-right:3px;}
  .banner--strip .brand-panel{left:371px;top:0;right:0;bottom:0;}
  .banner--strip .brand-name{left:12px;top:3px;font-size:10px;}
  .banner--strip .brand-name span + span{font-size:4.5px;letter-spacing:2px;margin-top:1px;}
  .banner--strip .site-url{left:13px;top:22px;font-size:8px;}
  .banner--strip .cta{left:14px;top:35px;width:72px;height:19px;font-size:10px;border-radius:3px;}
</style>
</head>
<body>
<div class="stage">

  <section class="banner banner--rect" aria-label="300 by 250 banner">
    <h1 class="headline">We Drive Phone Calls<br>&amp; Conversions</h1>
    <div class="device-art" role="img" aria-label="Responsive website shown on desktop monitor, tablet and phone"></div>
    <ul class="services">
      <li>Web Design</li><li>Local SEO</li><li>Pay-Per-Click</li><li>Social Media</li><li>Content Marketing</li>
    </ul>
    <div class="brand-panel">
      <p class="brand-name"><span>BRIGHTSIGNAL</span><span>MARKETING</span></p>
      <p class="site-url">www.yoursite.com</p>
      <a class="cta"><svg width="12" height="14" viewBox="0 0 12 14"><path d="M1 1 L1 12 L4 9 L6.5 13.5 L8.5 12.5 L6 8 L10 8 Z" fill="#111"/></svg>Learn More</a>
    </div>
  </section>

  <section class="banner banner--leader" aria-label="728 by 90 banner">
    <div class="device-art" role="img" aria-label="Responsive website shown on desktop monitor, tablet and phone"></div>
    <h2 class="headline">We Drive Phone Calls<br>&amp; Conversions</h2>
    <ul class="services">
      <li>Web Design</li><li>Local SEO</li><li>Pay-Per-Click</li><li>Social Media</li><li>Content Marketing</li>
    </ul>
    <div class="brand-panel">
      <p class="brand-name"><span>BRIGHTSIGNAL</span><span>MARKETING</span></p>
      <p class="site-url">www.yoursite.com</p>
      <a class="cta"><svg width="12" height="14" viewBox="0 0 12 14"><path d="M1 1 L1 12 L4 9 L6.5 13.5 L8.5 12.5 L6 8 L10 8 Z" fill="#111"/></svg>Learn More</a>
    </div>
  </section>

  <section class="banner banner--strip" aria-label="480 by 60 banner">
    <div class="device-art" role="img" aria-label="Responsive website shown on desktop monitor, tablet and phone"></div>
    <h2 class="headline">We Drive Phone Calls &amp; Conversions</h2>
    <ul class="services">
      <li>Web Design</li><li>Local SEO</li><li>Pay-Per-Click</li><li>Social Media</li><li>Content Marketing</li>
    </ul>
    <div class="brand-panel">
      <p class="brand-name"><span>BRIGHTSIGNAL</span><span>MARKETING</span></p>
      <p class="site-url">www.yoursite.com</p>
      <a class="cta"><svg width="8" height="10" viewBox="0 0 12 14"><path d="M1 1 L1 12 L4 9 L6.5 13.5 L8.5 12.5 L6 8 L10 8 Z" fill="#111"/></svg>Learn More</a>
    </div>
  </section>

</div>
</body>
</html>
```